Kestra Rowe - Contact/Landing Page

I need a landing page which will essentially be the page that customers will go to from the 'website' link on TLX listing. It will provide a short overview of services which need to be selectable. a little further down can capture some contact details followed by a large Submit Now button etc...

I have some icon/logo's that can be utilised at the bottom of the page as industry type references.

Target Market(s)

End of Lease Cleaning Services

Industry/Entity Type

Cleaning Service

Colors

Designer to choose colors to be used in the design.

Requirements
Must have
• As per description
Should not have
• Colours to match my website kestrarowe.com.au

```html
<!DOCTYPE html>
<html lang="en">
<head>
<meta charset="utf-8">
<title>Kestra Rowe – End of Lease Services</title>
<link href="https://fonts.googleapis.com/css2?family=Oswald:wght@400;500&family=Poppins:wght@400&display=swap" rel="stylesheet">
<style>
  :root {
    --brand: #1e9fd8;
    --brand-dark: #1b8cc2;
    --ink: #1f1f1f;
    --body: #333;
    --field: #efefef;
    --line: #222;
    --white: #fff;
    --badge: #c8c8c8;
  }
  * { box-sizing: border-box; margin: 0; padding: 0; }
  html, body { width: 1024px; height: 1200px; overflow: hidden; background: var(--white); }
  body { position: relative; font-family: "Poppins", sans-serif; color: var(--body); }

  .hero-photo {
    position: absolute; left: 0; top: 0; width: 1024px; height: 501px;
    background: linear-gradient(180deg, #a9d3ee 0%, #cfe5f3 25%, #7a7f88 45%, #8a6a5a 70%, #6d6b5c 100%);
  }
  .brand-mark {
    position: absolute; left: 0; width: 1024px; top: 50px; text-align: center;
    font-family: "Oswald", sans-serif; font-weight: 500; font-size: 24px; color: var(--brand);
    letter-spacing: 1px;
  }
  .title-box {
    position: absolute; left: 307px; top: 256px; width: 410px; height: 76px;
    background: var(--white); text-align: center;
  }
  .title-box h1 {
    font-family: "Oswald", sans-serif; font-weight: 500; font-size: 30px; color: var(--brand);
    letter-spacing: 6px; line-height: 36px; height: 36px; margin-top: 7px; padding-left: 6px;
    white-space: nowrap;
  }
  .subtitle {
    display: flex; align-items: center; justify-content: center; gap: 9px;
    font-size: 10px; line-height: 14px; color: var(--ink); margin-top: 6px; white-space: nowrap;
  }
  .subtitle::before, .subtitle::after { content: ""; width: 72px; height: 1px; background: var(--line); }

  .panel {
    position: absolute; left: 200px; top: 405px; width: 623px; height: 581px;
    background: var(--white); box-shadow: 0 10px 30px rgba(0,0,0,0.08);
  }
  .step-heading {
    position: absolute; left: 37px; width: 549px; display: flex; align-items: center; gap: 6px;
    font-family: "Oswald", sans-serif; font-size: 13.5px; color: var(--ink); white-space: nowrap;
  }
  .step-heading::before, .step-heading::after { content: ""; flex: 1; height: 1px; background: var(--line); }
  .step-heading .num { color: var(--brand); }
  .step-one { top: 24px; }
  .step-two { top: 253px; }

  .service {
    position: absolute; top: 54px; width: 191px; height: 175px; padding: 21px 0 0 15px;
    border: 1px solid transparent;
  }
  .service.is-selected { background: #f0f0f0; border-color: var(--brand); }
  .service-icon { width: 58px; height: 38px; display: block; }
  .service h2 {
    font-family: "Oswald", sans-serif; font-weight: 500; font-size: 13px; letter-spacing: 1.2px;
    color: var(--brand); margin-top: 16px; line-height: 1;
  }
  .service p { font-size: 8.3px; line-height: 13px; color: var(--body); margin-top: 6px; width: 165px; height: 26px; }
  .select-btn {
    display: flex; align-items: center; gap: 17px; width: 160px; height: 26px; margin-top: 11px;
    background: var(--brand); border-radius: 2px; padding-left: 7px;
    box-shadow: 0 5px 10px rgba(30,159,216,0.25);
    font-family: "Oswald", sans-serif; font-size: 9.5px; letter-spacing: 0.6px; color: var(--white);
  }
  .checkbox { width: 14px; height: 14px; background: var(--white); border-radius: 1px; display: flex; align-items: center; justify-content: center; }

  .field {
    position: absolute; background: var(--field); font-size: 8.5px; color: var(--ink);
    display: flex; align-items: center; justify-content: center;
  }
  .field.message { align-items: flex-start; padding-top: 9px; }
  .submit-btn {
    position: absolute; left: 248px; top: 485px; width: 127px; height: 42px;
    background: var(--brand); border-radius: 3px; box-shadow: 0 6px 12px rgba(30,159,216,0.25);
    color: var(--white); font-family: "Oswald", sans-serif; font-size: 9.5px; letter-spacing: 0.6px;
    display: flex; align-items: center; justify-content: center;
  }
  .contact-email {
    position: absolute; left: 0; width: 623px; top: 537px; text-align: center;
    font-family: "Oswald", sans-serif; font-weight: 400; font-size: 9.5px; letter-spacing: 0.4px; color: var(--ink);
  }

  .badges { position: absolute; top: 1018px; left: 253px; display: flex; gap: 16.5px; }
  .badge {
    width: 90px; height: 53px; border: 1px solid var(--badge);
    display: flex; align-items: center; justify-content: center;
  }
  .badge-shape { width: 58px; height: 22px; background: #d9d9d9; border-radius: 2px; }
  .footer {
    position: absolute; top: 1130px; left: 0; width: 1024px; text-align: center;
    font-family: "Oswald", sans-serif; font-weight: 400; font-size: 8px; letter-spacing: 0.3px; color: var(--ink);
  }
</style>
</head>
<body>
  <div class="hero-photo" role="img" aria-label="Photo of a smiling cleaning technician in a blue uniform giving a thumbs up in front of suburban brick houses"></div>
  <div class="brand-mark">Kestra Rowe</div>

  <header class="title-box">
    <h1>END OF LEASE SERVICES</h1>
    <div class="subtitle">Avail our Services in 2 Simple, Easy Steps!</div>
  </header>

  <main class="panel">
    <div class="step-heading step-one"><span><span class="num">Step 1.</span> Select a Service(s)</span></div>

    <div class="service" style="left:14px">
      <svg class="service-icon" viewBox="0 0 58 38" role="img" aria-label="Cleaning spray icon">
        <path d="M6 17 L29 0 L52 17 L52 36 L6 36 Z" fill="#b9b9b9"/>
        <rect x="22" y="10" width="14" height="26" rx="2" fill="var(--brand)"/>
        <line x1="0" y1="37" x2="58" y2="37" stroke="#222" stroke-width="1"/>
      </svg>
      <h2>CLEANING</h2>
      <p>All interior cleaning carried out to Property Management requirements.</p>
      <div class="select-btn"><span class="checkbox"></span>SELECT THIS OPTION</div>
    </div>

    <div class="service is-selected" style="left:216px">
      <svg class="service-icon" viewBox="0 0 58 38" role="img" aria-label="Carpet steam cleaner icon">
        <path d="M6 17 L29 0 L52 17 L52 36 L6 36 Z" fill="#b9b9b9"/>
        <rect x="12" y="18" width="34" height="16" rx="2" fill="var(--brand)"/>
        <line x1="0" y1="37" x2="58" y2="37" stroke="#222" stroke-width="1"/>
      </svg>
      <h2>CARPET CLEANING</h2>
      <p>Carpet Steam Cleaning to Australian Sandard AS 3733:1995.</p>
      <div class="select-btn"><span class="checkbox">
        <svg width="10" height="10" viewBox="0 0 10 10"><path d="M1.5 5.2 L4 7.5 L8.5 2.5" fill="none" stroke="var(--brand)" stroke-width="1.8"/></svg>
      </span>SELECT THIS OPTION</div>
    </div>

    <div class="service" style="left:418px">
      <svg class="service-icon" viewBox="0 0 58 38" role="img" aria-label="Pest control sprayer icon">
        <path d="M6 17 L29 0 L52 17 L52 36 L6 36 Z" fill="#b9b9b9"/>
        <rect x="18" y="12" width="22" height="22" rx="3" fill="var(--brand)"/>
        <line x1="0" y1="37" x2="58" y2="37" stroke="#222" stroke-width="1"/>
      </svg>
      <h2>PEST CONTROL</h2>
      <p>Mandatory requirement for pets on premises.</p>
      <div class="select-btn"><span class="checkbox"></span>SELECT THIS OPTION</div>
    </div>

    <div class="step-heading step-two"><span><span class="num">Step 2.</span> Enter your Details</span></div>

    <div class="field" style="left:109px;top:283px;width:198px;height:26px">First Name</div>
    <div class="field" style="left:317px;top:283px;width:197px;height:26px">Surname</div>
    <div class="field" style="left:109px;top:320px;width:198px;height:26px">Email</div>
    <div class="field" style="left:317px;top:320px;width:197px;height:26px">Phone</div>
    <div class="field" style="left:109px;top:357px;width:405px;height:27px">Suburb</div>
    <div class="field message" style="left:109px;top:395px;width:405px;height:80px">Message(Optional)</div>

    <div class="submit-btn">SUBMIT</div>
    <div class="contact-email">info@kestrarowe.com.au</div>
  </main>

  <section class="badges" aria-label="Industry certifications">
    <div class="badge"><span class="badge-shape"></span></div>
    <div class="badge"><span class="badge-shape"></span></div>
    <div class="badge"><span class="badge-shape"></span></div>
    <div class="badge"><span class="badge-shape"></span></div>
    <div class="badge"><span class="badge-shape"></span></div>
  </section>

  <footer class="footer">Kestra Rowe © 2021. All Rights Reserved.</footer>
</body>
</html>
```